Fresh & Clean *NEW* BUSINESS CARD Needed - OPTOMETRY Clinic/Optical

High-tech optometry practice with 3 doctors seeking new business card.  We provide eye exams, sell, designer glasses/contacts/specialty eyewear and treat ocular diseases.  For our business cards, we are seeking fresh, clean, and crisp design as we grow our team (staffing change).  Simply adding doctors is making the card look busy/cluttered.
 Looking for professional, less cluttered look yet still have our logo, doctor names, phone, address, and website....If possible!  :)
Names:
Marcia Trelford, O.D.
Ned Pallister, O.D.
Oona Ferrant, O.D.
Phone: 555-014-2738
Website: www.BrightLensHub.example
Address:  417 Garnet R. Holloway, College Station, TX 00000
Ultimately we have the main business card with all doctor sames and that card has two versions  (front is always the same).  The back has two designs (1) displays next appointment time/date, (2) for "general use" (non-appointment.)    I have attached what we have used in the past.  
We also need a design template for each team member in our practice with their name, title, and email.   Those should be designed with the "general use" back (see attached).
**Open to entirely new design so don't feel obligated to keep current format.  Need new perspective!  Also including our watermark and some other design features we have consistently used in past in our portfolio.  Included are two options for logos--vertical and horizontal.
**I also would like to remove "Member of Sight Alliance" on our logo if possible**
 Other image files available upon request.

Target Market(s)

New patient & Current Patients

Industry/Entity Type

Optometry

Contact Information for Business Card

High-tech optometry practice with 3 doctors seeking new business card.  We provide eye exams, sell, designer glasses/contacts/specialty eyewear and treat ocular diseases.  For our business cards, we are seeking fresh, clean, and crisp design as we grow our team (staffing change).  Simply adding doctors is making the card look busy/cluttered.  Looking for professional, less cluttered look yet still have our logo, doctor names, phone, address, and website....If possible!  :) Names: Marcia Trelford, O.D. Ned Pallister, O.D. Oona Ferrant, O.D. Phone: 555-014-2738 Website: www.BrightLensHub.example Address:  417 Garnet R. Holloway, College Station, TX 00000 Ultimately we have the main business card with all doctor sames and that card has two versions  (front is always the same).  The back has two designs (1) displays next appointment time/date, (2) for "general use" (non-appointment.)    I have attached what we have used in the past.   We also need a design template for each team member in our practice with their name, title, and email.   Those should be designed with the "general use" back (see attached). **Open to entirely new design so don't feel obligated to keep current format.  Need new perspective!  Also including our watermark and some other design features we have consistently used in past in our portfolio.  Included are two options for logos--vertical and horizontal. **I also would like to remove "Member of Sight Alliance" on our logo if possible**  Other image files available upon request.

Font styles to use
Other font styles liked:
• We have used Montserrat / Yellowtail in the past

Colors

Designer to choose colors to be used in the design.

Requirements
Must have
• Clean & Fresh Design with Logo / Info provided in description. Horizontal orientation. **I have included the CMYK colors we currently have in our logo.
Should not have
• Cluttered

```html
<!DOCTYPE html>
<html lang="en">
<head>
<meta charset="utf-8">
<title>BrightLens Hub – Business Card</title>
<link href="https://fonts.googleapis.com/css2?family=Montserrat:wght@400;500;600;700&display=swap" rel="stylesheet">
<style>
  :root {
    --navy: #001f6b;
    --page: #e3e3e3;
    --white: #ffffff;
    --ink: #1a1a1a;
    --soft-text: #e6eaf4;
    --brand-grey: #6d6d6d;
    --faint: #f1f1f1;
    --stripe: #e4e6ec;
  }
  * { margin: 0; padding: 0; box-sizing: border-box; }
  html, body { width: 1200px; height: 1000px; overflow: hidden; }
  body {
    background: var(--page);
    font-family: "Montserrat", sans-serif;
    position: relative;
  }
  .card {
    position: absolute;
    left: 309px;
    width: 582px;
    height: 330px;
    overflow: hidden;
    background: var(--white);
  }
  /* Front */
  .card-front { top: 159px; }
  .front-panel {
    position: absolute; left: 0; top: 0; width: 100%; height: 294px;
    background: var(--navy);
  }
  .brand-box {
    position: absolute; left: 210px; top: 0; width: 158px; height: 107px;
    background: var(--white);
    display: flex; align-items: center; justify-content: center;
  }
  .brand-name {
    font-size: 19px; font-weight: 400; color: var(--brand-grey);
    text-align: center; line-height: 1.05; letter-spacing: 0.5px;
  }
  .doctor-list {
    position: absolute; left: 0; top: 141px; width: 100%;
    text-align: center; color: var(--soft-text);
    font-size: 17px; font-weight: 500; letter-spacing: 0.1px;
  }
  .contact-list {
    position: absolute; left: 152px; top: 193px; list-style: none;
    color: var(--soft-text); font-size: 13.5px; font-weight: 500;
  }
  .contact-list li { display: flex; align-items: center; height: 28.5px; }
  .contact-list svg { width: 19px; height: 19px; margin-right: 10px; flex: none; }
  .address-strip {
    position: absolute; left: 0; top: 294px; width: 100%; height: 36px;
    display: flex; align-items: center; justify-content: center;
    font-size: 14.5px; font-weight: 600; color: var(--ink);
  }
  /* Back */
  .card-back { top: 512px; }
  .back-art { position: absolute; left: 0; top: 0; }
  .appointment-title {
    position: absolute; left: 76px; top: 16px;
    color: var(--soft-text); font-size: 18.5px; font-weight: 600;
  }
  .field-label {
    position: absolute; top: 143px; font-size: 17px; font-weight: 700; color: var(--ink);
  }
  .field-date { left: 51px; }
  .field-time { left: 324px; }
  .notice {
    position: absolute; left: 0; top: 247px; width: 100%; height: 83px;
    background: var(--navy); color: var(--soft-text);
    display: flex; align-items: center; justify-content: center;
    text-align: center; font-size: 14.5px; font-weight: 500; line-height: 23px;
  }
</style>
</head>
<body>
  <section class="card card-front">
    <div class="front-panel">
      <div class="brand-box">
        <div class="brand-name">brightlens<br>hub</div>
      </div>
      <p class="doctor-list">Marcia Trelford, O.D. | Ned Pallister, O.D. | Oona Ferrant, O.D.</p>
      <ul class="contact-list">
        <li>
          <svg viewBox="0 0 20 20" fill="none" stroke="#e6eaf4" stroke-width="1.3"><circle cx="10" cy="10" r="8"/><ellipse cx="10" cy="10" rx="3.5" ry="8"/><path d="M2 10h16M3.5 6h13M3.5 14h13"/></svg>
          www.BrightLensHub.example
        </li>
        <li>
          <svg viewBox="0 0 20 20" fill="none" stroke="#e6eaf4" stroke-width="1.3" stroke-linejoin="round"><path d="M5 2.5l3 3.2-1.8 2.2c1 2.2 2.7 3.9 4.9 4.9l2.2-1.8 3.2 3-1.8 2.5C9 16 4 11 2.5 4.3z"/></svg>
          555-014-2738
        </li>
        <li>
          <svg viewBox="0 0 20 20" fill="none" stroke="#e6eaf4" stroke-width="1.3"><rect x="1.5" y="4" width="17" height="12"/><path d="M1.5 4l8.5 7 8.5-7M1.5 16l6-6M18.5 16l-6-6"/></svg>
          MTrelford@BrightLensHub.example
        </li>
      </ul>
    </div>
    <div class="address-strip">417 Garnet R. Holloway, College Station, Texas</div>
  </section>

  <section class="card card-back">
    <svg class="back-art" width="582" height="330" viewBox="0 0 582 330">
      <rect x="420" y="0" width="162" height="55" fill="#f3f3f3"/>
      <polygon points="540,0 582,0 582,28 512,170 470,150" fill="var(--faint)"/>
      <polygon points="582,46 582,205 520,175" fill="var(--faint)"/>
      <polygon points="0,0 388,0 351,55 0,55" fill="var(--navy)"/>
      <polygon points="388,0 403,0 366,55 351,55" fill="var(--stripe)"/>
      <polygon points="403,0 421,0 396,55 363,55" fill="var(--navy)"/>
      <circle cx="287" cy="148" r="66" fill="none" stroke="#e9e9e9" stroke-width="6"/>
    </svg>
    <h2 class="appointment-title">Your Next Appointment</h2>
    <span class="field-label field-date">Date:</span>
    <span class="field-label field-time">Time:</span>
    <p class="notice">If you are unable to keep your appointment<br>kindly give us 24 hours notice.</p>
  </section>
</body>
</html>
```